Business card design needed

Family General Practitioner/ Family Physician.
Logo is the logo of the Crestmoor Guild of Family Clinicians Australia
http://kvplm.tarevo.edu.au/PictureGallery/logos/pages/CGFC%20logo_jpg.htm

Reason: Just a bit more time to make changes and the weekend for me to look at things closely and to choose. Thanks, Lumi

Thanks for all the submissions. So many of them are really works of art. Not one of them are not good. The ones that I am eliminating are the ones that I think are not suitable for me personally only, and because if I don't, it makes it very difficult to decide as many of you are also sending me slight variations of a card. I have just decided to choose a second place card too. Can't thank you all enough. Good luck, Lumi. P.S - Working today till 10 pm as the card says :-), so probably won't be able to give a feedback till late Saturday night or Sunday morning here in Sydney, Australia. 

Reason: Just added a second place to the budget and realised that Australia is ahead of the rest of the world in the time zone (only :-) - don't want to offend anyone or start a debate!! ) , so Monday deadline will mean it will be a weekend for the rest of the world. Just wanted to give everyone more time to submit their best, especially since I will be picking a second card too. Can't thank everyone enough for the submissions. P.S - Not keen on photos on the card.

Contact Information for Business Card

Dr. Lumi Harcourt M.B.B.S., F.C.G.F.C
Family General Practitioner
Address, timings, phone and fax number on the back.

Requirements
Must have
• Timings
Mon 7 am - 7 pm
Tues 7 am - 12 pm
Wed 7 am - 10 pm
Thurs 7 am - 12 pm
Fri 7 am - 8 pm
Sat 8 am - 10 pm
Sun - Off

```html
<!DOCTYPE html>
<html lang="en">
<head>
<meta charset="utf-8">
<title>Dr. Lumi Harcourt – Business Card Back</title>
<link rel="stylesheet" href="https://fonts.googleapis.com/css2?family=Jost:wght@400;500&display=swap">
<style>
  :root {
    --card-green: #43f495;
    --ink: #111;
    --paper: #ffffff;
    --accent-dark: #1f6a3f;
  }
  html, body {
    margin: 0;
    padding: 0;
    width: 1200px;
    height: 741px;
    overflow: hidden;
    background: var(--card-green);
  }
  .card {
    position: relative;
    width: 1200px;
    height: 741px;
    background: var(--card-green);
    font-family: "Jost", "Futura", sans-serif;
    color: var(--paper);
  }
  .hours-title {
    position: absolute;
    left: 873px;
    top: 44px;
    margin: 0;
    font-size: 22px;
    font-weight: 400;
    color: var(--ink);
    letter-spacing: 0.2px;
  }
  .hours-title strong { font-weight: 500; }
  .hours {
    position: absolute;
    left: 808px;
    top: 94px;
    width: 326px;
    margin: 0;
    padding: 0;
    list-style: none;
  }
  .hours li {
    display: flex;
    justify-content: space-between;
    height: 51.5px;
    font-size: 35px;
    font-weight: 400;
    line-height: 48px;
    letter-spacing: -0.3px;
  }
  .hours .closed { padding-right: 80px; }
  .address {
    position: absolute;
    left: 61px;
    top: 563px;
    margin: 0;
    font-size: 22.5px;
    color: var(--ink);
    letter-spacing: 0.9px;
    white-space: nowrap;
  }
  .contact-band {
    position: absolute;
    left: 39px;
    top: 601px;
    width: 1161px;
    height: 57px;
    background: var(--paper);
  }
  .contact-band p {
    margin: 0;
    padding-left: 22px;
    font-size: 34px;
    line-height: 57px;
    color: var(--ink);
    white-space: nowrap;
  }
  .contact-band .gap { margin-left: 22px; }
  .band-bracket {
    position: absolute;
    left: 17px;
    top: 589px;
  }
</style>
</head>
<body>
  <main class="card">
    <h2 class="hours-title">WORKING <strong>HOURS</strong></h2>
    <ul class="hours">
      <li><span>MON</span><span>7 AM - &nbsp;7 PM</span></li>
      <li><span>TUES</span><span>7 AM - 12 PM</span></li>
      <li><span>WED</span><span>7 AM - 10 PM</span></li>
      <li><span>THUR</span><span>7 AM - 12 PM</span></li>
      <li><span>FRI</span><span>7 AM - &nbsp;8 PM</span></li>
      <li><span>SAT</span><span>8 AM - 10 PM</span></li>
      <li><span>SUN</span><span class="closed">OFF</span></li>
    </ul>

    <p class="address">UPPER LEVEL, FOUNTAIN COURT, BRANDMERE TOWERS SHOPPING CENTER, ELMVALE, NSW 2199</p>

    <svg class="band-bracket" width="24" height="84" viewBox="0 0 24 84" aria-hidden="true">
      <defs>
        <linearGradient id="bracketShade" x1="0" x2="1">
          <stop offset="0" stop-color="#1f6a3f" stop-opacity="0.5"/>
          <stop offset="1" stop-color="#1f6a3f" stop-opacity="0"/>
        </linearGradient>
      </defs>
      <rect x="4" y="2" width="18" height="80" fill="url(#bracketShade)"/>
      <rect x="2" y="0" width="3" height="82" fill="var(--accent-dark)"/>
      <rect x="2" y="0" width="20" height="2.5" fill="var(--accent-dark)"/>
    </svg>

    <div class="contact-band">
      <p>PH: &nbsp;02 5550 1400 <span class="gap">FAX: 02 5550 1233</span></p>
    </div>
  </main>
</body>
</html>
```